Scheduled Servicing Forms

Lumenridge Systems requires two schedule servicing forms to be created on designer templates for our engineers to complete when servicing customers. We will complete these forms on a periodic basis, and send to the customer on completion of the work.
We have two forms that need to be created:
• Hybrid Cloud Customer Service
• Norvex Cloud Customer Service
Please do not reference our website for ideas as its about to change. “Specialised Consulting” is our new go to market, not “Charting the Frontiers of Computing. Our new website (still under development) is available at https://lumenridgesystems.qxv.net.au and will be officially launched shortly.
Our company theme is “Blue” and we want to keep a blue theme for the work.
Please ensure there is “Ample” space for engineers to write comments next to each audit item.
We have uploaded examples of the content that needs to be created for both form in Word and Excel format.
The designer must upload the source files (not just PDF) so we can edit the content on the forms at a later date.
The forms must be in standard A4 size (multiple pages).

```html
<!DOCTYPE html>
<html lang="en">
<head>
<meta charset="utf-8">
<title>Lumenridge Systems – Scheduled Service Checklist</title>
<link rel="stylesheet" href="https://fonts.googleapis.com/css2?family=Barlow:ital,wght@0,400;0,500;0,600;1,400&display=swap">
<style>
  :root {
    --bg: #d6d7d9;
    --paper: #ffffff;
    --brand-blue: #1f4e9f;
    --navy-deep: #050d1c;
    --navy-mid: #0d2545;
    --row-tint: #e8f0f9;
    --ink: #1b1b1b;
    --line: #333333;
    --box-edge: #4a4a4a;
  }
  * { box-sizing: border-box; margin: 0; padding: 0; }
  html, body { width: 1000px; height: 1200px; overflow: hidden; }
  body {
    background: var(--bg);
    font-family: "Barlow", Arial, sans-serif;
    color: var(--ink);
  }
  .sheet {
    position: absolute;
    left: 75px; top: 0;
    width: 850px; height: 1200px;
    background: var(--paper);
  }
  .masthead {
    position: absolute; left: 0; top: 0;
    width: 100%; height: 125px;
    background: radial-gradient(ellipse at 50% 55%, #173a66 0%, var(--navy-mid) 40%, var(--navy-deep) 100%);
    display: flex; align-items: center; justify-content: center;
  }
  .brand {
    display: flex; align-items: center; gap: 14px;
    color: #ffffff; font-weight: 600; font-size: 32px; letter-spacing: 2px;
    text-transform: uppercase;
  }
  .brand-mark { width: 26px; height: 26px; background: #ffffff; }
  .form-subtitle {
    position: absolute; top: 142px; width: 100%;
    text-align: center; font-size: 19px; font-weight: 500;
  }
  .form-title {
    position: absolute; top: 174px; left: 262px;
    width: 325px; height: 33px;
    background: var(--brand-blue); color: #fff;
    font-size: 23px; font-weight: 500;
    display: flex; align-items: center; justify-content: center;
  }
  .field {
    position: absolute; top: 226px;
    font-size: 19px; font-weight: 500;
    display: flex; align-items: flex-end; gap: 4px;
  }
  .field-line { border-bottom: 1px solid var(--line); height: 20px; }
  .field--customer { left: 21px; }
  .field--customer .field-line { width: 243px; }
  .field--date { left: 612px; }
  .field--date .field-line { width: 166px; }
  .checklist { position: absolute; left: 21px; top: 262px; width: 807px; }
  .checklist-head {
    height: 29px; background: var(--brand-blue); color: #fff;
    font-size: 17px; position: relative;
  }
  .checklist-head span { position: absolute; top: 4px; }
  .head-check { left: 50px; }
  .head-result { left: 514px; }
  .check-row { position: relative; height: 81px; font-size: 13px; line-height: 1.3; }
  .check-row:nth-child(odd) { background: var(--row-tint); }
  .check-task { position: absolute; left: 14px; top: 14px; width: 245px; }
  .check-task em { font-style: italic; }
  .opt { position: absolute; top: 14px; text-align: center; width: 28px; }
  .opt-yes { left: 283px; }
  .opt-no { left: 333px; }
  .opt .box {
    display: block; width: 20px; height: 20px; margin: 9px auto 0;
    border: 1px solid var(--box-edge); background: #fff;
  }
  .comment { position: absolute; left: 389px; top: 14px; }
  .expiry { position: absolute; left: 391px; top: 55px; display: flex; align-items: flex-end; gap: 4px; }
  .expiry .field-line { width: 104px; height: 14px; }
</style>
</head>
<body>
<main class="sheet">
  <header class="masthead" role="img" aria-label="Dark blue header band with faint network-line background and company name">
    <div class="brand"><span class="brand-mark"></span>Lumenridge Systems</div>
  </header>

  <p class="form-subtitle">Norvex Hybrid/On-Premise</p>
  <h1 class="form-title">Scheduled Service Checklist</h1>

  <div class="field field--customer">Customer:<span class="field-line"></span></div>
  <div class="field field--date">Date:<span class="field-line"></span></div>

  <section class="checklist">
    <div class="checklist-head">
      <span class="head-check">Maintenance Check</span>
      <span class="head-result">Result</span>
    </div>
    <div class="checklist-rows">
      <div class="check-row">
        <p class="check-task">Active backup for all Norvex 360 accounts <em>(manual check)</em> - ensuring all items are included in the job</p>
        <span class="opt opt-yes">YES<span class="box"></span></span><span class="opt opt-no">No<span class="box"></span></span>
        <span class="comment">Comment:</span>
      </div>
      <div class="check-row">
        <p class="check-task">Test restore from server backup</p>
        <span class="opt opt-yes">YES<span class="box"></span></span><span class="opt opt-no">No<span class="box"></span></span>
        <span class="comment">Comment:</span>
      </div>
      <div class="check-row">
        <p class="check-task">Test restore of an email</p>
        <span class="opt opt-yes">YES<span class="box"></span></span><span class="opt opt-no">No<span class="box"></span></span>
        <span class="comment">Comment:</span>
      </div>
      <div class="check-row">
        <p class="check-task">Test restore of ShareDeck file</p>
        <span class="opt opt-yes">YES<span class="box"></span></span><span class="opt opt-no">No<span class="box"></span></span>
        <span class="comment">Comment:</span>
      </div>
      <div class="check-row">
        <p class="check-task">Log into Antivirus products<br><em>(ensure all endpoint devices have active antivirus and are up to date)</em></p>
        <span class="opt opt-yes">YES<span class="box"></span></span><span class="opt opt-no">No<span class="box"></span></span>
        <span class="comment">Comment:</span>
      </div>
      <div class="check-row">
        <p class="check-task">Check Spam filters</p>
        <span class="opt opt-yes">YES<span class="box"></span></span><span class="opt opt-no">No<span class="box"></span></span>
        <span class="comment">Comment:</span>
      </div>
      <div class="check-row">
        <p class="check-task">Check that all users have MFA enabled</p>
        <span class="opt opt-yes">YES<span class="box"></span></span><span class="opt opt-no">No<span class="box"></span></span>
        <span class="comment">Comment:</span>
      </div>
      <div class="check-row">
        <p class="check-task">Review N360 Risk Detections</p>
        <span class="opt opt-yes">YES<span class="box"></span></span><span class="opt opt-no">No<span class="box"></span></span>
        <span class="comment">Comment:</span>
      </div>
      <div class="check-row">
        <p class="check-task">Confirm Audit Log enabled</p>
        <span class="opt opt-yes">YES<span class="box"></span></span><span class="opt opt-no">No<span class="box"></span></span>
        <span class="comment">Comment:</span>
        <span class="expiry">Expiry Date:<span class="field-line"></span></span>
      </div>
      <div class="check-row">
        <p class="check-task">Review N360 license expiry dates</p>
        <span class="opt opt-yes">YES<span class="box"></span></span><span class="opt opt-no">No<span class="box"></span></span>
        <span class="comment">Comment:</span>
      </div>
      <div class="check-row">
        <p class="check-task">Review external sharing in ShareDeck/OneVault</p>
        <span class="opt opt-yes">YES<span class="box"></span></span><span class="opt opt-no">No<span class="box"></span></span>
        <span class="comment">Comment:</span>
      </div>
    </div>
  </section>
</main>
</body>
</html>
```